Book cover: Stormy Days Survival for Kids (A5)

I have a book called Stormy Days Survival for Teens. It is a book for teenagers which gives them tips and tactics on how to survive life's challenges regarding friends, family, feelings, relationships and hard stuff in life generally. I will upload the cover of this book but you can see it on my past jobs as one of the designers her eon Pixel Bazaar did it for me.
I have a new book I've written called Stormy Days Survival for Kids. This is a parallel book to Stormy Days Survival for Teens, but it is specifically for 8 to 12 or 13 year olds, rather than for older teens.
A very important aspect of this job is that it SHOULD MATCH in some strong way - the Stormy Days Survival for Teens book. I will be selling them together, displaying them together and I want them to look like two of a pair. It might be that you use the same image as the first book but change the colour of the image so that it is bright orange and green perhaps? Or that there is another image but in the image is placed in the exact same position across the book as the first book. It needs to look like the books are by the same author.
However, I would like this one to look a bit "younger", more kid friendly. For example, a font that looks like it is for kids, or kids' writing perhaps.
I dont want to have photos on the book, and I dont think I want cartoons or drawings - because I'm not sure how this will tie in with the first book.
I want it to look modern, fresh and designed specifically for kids. The text needs to be:
Stormy Days Survival - For Kids!
Tips and ideas for 8 to 13 year olds about how to stay cool, calm and confident on even the toughest days!
The back cover is going to mostly just have the table of contents listed and a blurb, with one or two cartoons which I will supply. I am keen to pick a designer to just do the front cover first and will ask them to do the back cover later.
UPDATED: I have attached three files with fonts that I like.

```html
<!DOCTYPE html>
<html lang="en">
<head>
<meta charset="utf-8">
<title>Stormy Days Survival for Kids – Book Cover</title>
<link rel="stylesheet" href="https://fonts.googleapis.com/css2?family=Cabin+Sketch:wght@400;700&family=Inter:wght@300;400&display=swap">
<style>
  :root {
    --paper: #ffffff;
    --frame: #9a9693;
    --pencil: #8e8680;
    --sun-fill: #f4f7a6;
    --sun-edge: #2a2a2a;
    --hill-inner: #f8e1ea;
    --hill-outer: #efd3dc;
    --hill-edge: #6e6a66;
    --figure: #ece8e4;
    --author: #4e4a47;
  }
  html, body {
    margin: 0;
    padding: 0;
    overflow: hidden;
    background: var(--paper);
  }
  .cover {
    position: relative;
    width: 845px;
    height: 1200px;
    overflow: hidden;
    background: var(--paper);
  }
  .cover__art {
    position: absolute;
    inset: 0;
  }
  .title {
    position: absolute;
    left: 42px;
    top: 200px;
    margin: 0;
    font-family: "Cabin Sketch", cursive;
    font-weight: 400;
    color: var(--pencil);
    text-transform: uppercase;
    line-height: 1;
  }
  .title__line { display: block; }
  .title__line--first { font-size: 88px; letter-spacing: 1px; }
  .title__line--second { font-size: 70px; margin: 34px 0 0 52px; }
  .title__line--third { font-size: 66px; margin: 30px 0 0 14px; letter-spacing: 1px; }
  .subtitle {
    position: absolute;
    left: 412px;
    top: 626px;
    margin: 0;
    font-family: "Cabin Sketch", cursive;
    font-weight: 400;
    font-size: 62px;
    color: var(--pencil);
    text-transform: uppercase;
    line-height: 1;
  }
  .tagline {
    position: absolute;
    left: 70px;
    top: 860px;
    width: 700px;
    margin: 0;
    font-family: "Cabin Sketch", cursive;
    font-weight: 400;
    font-size: 30px;
    line-height: 1.35;
    color: var(--pencil);
    text-align: center;
  }
  .figure {
    position: absolute;
    left: 170px;
    top: 632px;
    width: 86px;
    height: 148px;
    border-radius: 40px 40px 6px 6px;
    background: var(--figure);
  }
  .author {
    position: absolute;
    right: 50px;
    top: 1050px;
    text-align: right;
    font-family: "Inter", sans-serif;
    color: var(--author);
  }
  .author__name {
    margin: 0;
    font-size: 33px;
    font-weight: 300;
    letter-spacing: 0.3px;
  }
  .author__role {
    margin: 18px 22px 0 0;
    font-size: 17px;
    font-weight: 300;
  }
</style>
</head>
<body>
<main class="cover">
  <svg class="cover__art" width="845" height="1200" viewBox="0 0 845 1200" aria-hidden="true">
    <path class="ground-outer" d="M0 785 C 120 735, 260 716, 340 718 C 520 722, 700 760, 845 790 L845 1200 L0 1200 Z" fill="var(--hill-outer)"/>
    <rect class="panel" x="26" y="36" width="789" height="1119" rx="12" fill="var(--paper)"/>
    <clipPath id="panel-clip"><rect x="26" y="36" width="789" height="1119" rx="12"/></clipPath>
    <path class="ground-inner" clip-path="url(#panel-clip)" d="M0 785 C 120 735, 260 716, 340 718 C 520 722, 700 760, 845 790 L845 1200 L0 1200 Z" fill="var(--hill-inner)"/>
    <path class="hill-edge" d="M0 785 C 120 735, 260 716, 340 718 C 520 722, 700 760, 845 790" fill="none" stroke="var(--hill-edge)" stroke-width="3" stroke-dasharray="1 1.5"/>
    <rect class="frame" x="26" y="36" width="789" height="1119" rx="12" fill="none" stroke="var(--frame)" stroke-width="3"/>
  </svg>

  <svg class="cover__art" width="845" height="1200" viewBox="0 0 845 1200" role="img" aria-label="Large pale yellow sun illustration in the top right corner">
    <circle class="sun" cx="652" cy="188" r="220" fill="var(--sun-fill)" stroke="var(--sun-edge)" stroke-width="2"/>
  </svg>

  <h1 class="title">
    <span class="title__line title__line--first">Stormy</span>
    <span class="title__line title__line--second">Days</span>
    <span class="title__line title__line--third">Survival...</span>
  </h1>
  <p class="subtitle">(For Kids)</p>

  <div class="figure" role="img" aria-label="Small drawn figure sitting on the hill"></div>

  <p class="tagline">Tips and ideas for 8 to 13 year olds about how to stay cool, calm and confident on even the toughest days!</p>

  <div class="author">
    <p class="author__name">Maren Tollefsen</p>
    <p class="author__role">clinical psychologist</p>
  </div>
</main>
</body>
</html>
```